Quorlify Business Card

We require a stunning business card for Quorlify - a new digital marketing agency. The logo provided was designed by a graphic designer here on Artboxly.

www.quorlify-example.com - "Get more sales online"

What we do:
The business delivers website optimisation (Web design, social media strategy, digital strategies, SEO, PPC, conversion optimisation, email marketing) to get businesses more sales online.

The card must match the brand style which can be found on this website template:

http://layoutmarket.example/item/brightline-adaptive-versatile-layout/full_screen_preview/9137462

It must have 'wow' factor so that you'll never forget Quorlify - We're open to any materials, textures you think will work.

We don't want a boring run of the mill design - I can knock that up in Photoshop myself or use a template solution. It should be timeless and only need replacing should the contact details change.

The design should be eye catching, future proof, exceptionally chic, classy and oozing authority and confidence. Quorlify services must not look cheap.

Here's some brilliant designs to point you in the right direction:

http://tidyprints.example/30-remarkable-calling-cards/

The spec is for double sided, but we're open to your ideas. If it's going on an opaque or see through card, then of course a single side is preferable. Using creativity and thought on the medium for the card - shape - texture is desirable.

The strapline for the business is "Get more business online" please submit with / without strapline.
Updates

Please only submit your best 1-3 designs initially.

Target Market(s)

Business 2 Business - Local SMEs
Local professionals - Doctors, Dentists, Financials, Bespoke Retailers, Property companies - anyone with a decent budget to spend on digital marketing services and a high margin product or service to sell.

Industry/Entity Type

Graphic Designer

Requirements
Must have
• Text:
• name: Tom Vandlow
• position Digital Marketing Director
• mobile 07951 238 604
• website www.quorlify-example.com
Nice to have
• Check See http://tidyprints.example/30-remarkable-calling-cards/ for ideas.
• LinkedIn and Twitter usernames if there is space and it works on the design.

```html
<!DOCTYPE html>
<html lang="en">
<head>
<meta charset="utf-8">
<title>Quorlify Business Card</title>
<link rel="stylesheet" href="https://fonts.googleapis.com/css2?family=Questrial&display=swap">
<style>
  :root {
    --stage: #2e2f31;
    --card-white: #ffffff;
    --brand-teal: #1f4b5c;
    --brand-teal-deep: #0f4656;
    --brand-teal-emboss: #0b3a48;
    --brand-coral: #e9543f;
    --font-main: "Questrial", "Century Gothic", sans-serif;
  }
  * { box-sizing: border-box; margin: 0; padding: 0; }
  html, body {
    width: 1200px;
    height: 900px;
    overflow: hidden;
    background: var(--stage);
    font-family: var(--font-main);
  }
  .canvas {
    position: relative;
    width: 1200px;
    height: 900px;
  }
  .card {
    position: absolute;
    top: 300px;
    width: 520px;
    height: 300px;
    border-radius: 3px;
    box-shadow: 0 10px 30px rgba(0,0,0,0.45);
  }
  /* Back side */
  .card-back {
    left: 50px;
    background: var(--brand-teal-deep);
    display: flex;
    align-items: center;
    justify-content: center;
  }
  .back-wordmark {
    display: flex;
    align-items: center;
    gap: 14px;
    color: var(--brand-teal-emboss);
    font-size: 78px;
    letter-spacing: 1px;
  }
  .back-wordmark .mark-dot {
    width: 40px;
    height: 40px;
    border-radius: 50%;
    background: var(--brand-teal-emboss);
  }
  /* Front side */
  .card-front {
    left: 630px;
    background: var(--card-white);
  }
  .front-logo {
    position: absolute;
    left: 34px;
    top: 132px;
  }
  .wordmark {
    display: flex;
    align-items: center;
    gap: 8px;
    color: var(--brand-teal);
    font-size: 36px;
    line-height: 1;
  }
  .wordmark .mark-dot {
    width: 18px;
    height: 18px;
    border-radius: 50%;
    background: var(--brand-coral);
  }
  .strapline {
    margin-top: 6px;
    margin-left: 26px;
    font-size: 9px;
    color: var(--brand-teal);
    letter-spacing: 0.3px;
  }
  .contact-block {
    position: absolute;
    left: 318px;
    top: 40px;
    width: 190px;
    color: var(--brand-teal);
    font-size: 11px;
    line-height: 1.35;
  }
  .person-name {
    color: var(--brand-coral);
    font-size: 17px;
    line-height: 1.1;
    text-transform: uppercase;
    letter-spacing: 0.5px;
    font-weight: 400;
  }
  .person-role {
    color: var(--brand-coral);
    font-size: 9.5px;
    text-transform: uppercase;
    letter-spacing: 0.5px;
    margin-bottom: 16px;
    white-space: nowrap;
  }
  .contact-list { list-style: none; margin-bottom: 16px; }
  .contact-list li { display: flex; gap: 10px; white-space: nowrap; }
  .contact-label { color: var(--brand-coral); width: 8px; }
  .address { font-style: normal; white-space: nowrap; }
</style>
</head>
<body>
<main class="canvas">
  <section class="card card-back" aria-label="Card back">
    <div class="back-wordmark">
      <span class="mark-dot"></span>
      <span>Quorlify</span>
    </div>
  </section>

  <section class="card card-front" aria-label="Card front">
    <div class="front-logo">
      <div class="wordmark">
        <span class="mark-dot"></span>
        <span>Quorlify</span>
      </div>
      <p class="strapline">Get more business online</p>
    </div>

    <div class="contact-block">
      <h1 class="person-name">Tom<br>Vandlow</h1>
      <p class="person-role">Digital Marketing Director</p>
      <ul class="contact-list">
        <li><span class="contact-label">p</span><span>888 412 30 57</span></li>
        <li><span class="contact-label">m</span><span>07951 238 604</span></li>
        <li><span class="contact-label">e</span><span>tvandlow@quorlify-example.com</span></li>
      </ul>
      <address class="address">
        48 Harlow Lane<br>
        Brookfield, New York 12406<br>
        www.quorlify-example.com
      </address>
    </div>
  </section>
</main>
</body>
</html>
```